IT Consulting Site Revamping for Varnel

I've put a skeleton together on my website, but realize I need some help (it's http://pilot.varnel-example.ca).
I've pulled together tidbits from other websites, but really need my site to be cleaned up, and really spruced up.
I primarily focus on the IT needs of small to medium size businesses, taking care of everything from their servers and networks down to their workstations.
I also want a page listing the vendors (and logos) that I work with including Brontisoft, QZWare, Pelvar, Fusk, TQ, ZRL, WUBE, Morva, Trelagate.
There should also be a simple form to get a quote that will email me.
The final design should communicate strength and reliability.
I would like this to be a fully functional website, that I can upload to Plimba Pages, with the same sort of pages that are existing on http://pilot.varnel-example.ca
Updates
Hey everyone,
Hi everyone,
Reason: Hi all,
There are some designers that would like to submit some new designs, so I'm extending the deadline.
Thanks,
Target Market(s)
Small to medium size business owners. This will primarily be males who work in the oil and gas industry.
Industry/Entity Type
Consulting
Look and feel
Each slider illustrates characteristics of the customer's brand and the style your logo design should communicate.

```html
<!DOCTYPE html>
<html lang="en">
<head>
<meta charset="utf-8">
<title>Varnel Solutions</title>
<link href="https://fonts.googleapis.com/css2?family=PT+Sans:wght@400;700&family=Arimo:wght@400;700&display=swap" rel="stylesheet">
<style>
:root{
  --blue:#1a7fc4;
  --blue-dark:#0b6bb0;
  --blue-light:#3fa6e6;
  --footer:#0a7cc9;
  --ink:#333;
  --ink-soft:#555;
  --grey-bg:#ececec;
  --line:#d6d6d6;
  --red:#d0021b;
  --white:#fff;
}
*{margin:0;padding:0;box-sizing:border-box}
html,body{width:710px;height:1200px;overflow:hidden;background:var(--white)}
body{position:relative;font-family:"Arimo",Arial,sans-serif;color:var(--ink)}
.abs{position:absolute}
/* header */
.site-header{left:0;top:0;width:710px;height:96px;border-top:3px solid var(--blue);background:linear-gradient(#fafafa,#fff);border-bottom:1px solid var(--line)}
.brand{left:16px;top:18px;display:flex;align-items:center;gap:10px}
.brand-mark{width:56px;height:56px;border-radius:50%;background:var(--blue)}
.brand-name{font-family:"PT Sans",sans-serif;font-weight:700;font-size:34px;color:var(--blue);line-height:1}
.brand-sub{font-family:"PT Sans",sans-serif;font-size:11px;letter-spacing:5px;color:var(--blue);display:block;margin-top:2px}
.call{right:44px;top:12px;font-size:11px;color:var(--blue)}
.call b{font-size:14px;font-style:italic;color:var(--blue-dark);margin-left:4px}
.nav{left:294px;top:68px;display:flex;align-items:center;font-family:"PT Sans",sans-serif;font-size:11px;color:#333}
.nav span{margin-right:34px}
.nav svg{margin-right:14px}
/* hero */
.hero{left:0;top:97px;width:710px;height:266px;background:linear-gradient(90deg,#e4e4e4,#f4f4f4 50%,#ececec)}
.hero-photo{left:350px;top:3px;width:331px;height:261px;background:linear-gradient(135deg,#dfe6ec,#b9c4cf 45%,#6d7a88 75%,#c9ced4)}
.hero h1{left:26px;top:66px;font-family:"PT Sans",sans-serif;font-size:21px;color:var(--blue);letter-spacing:.5px}
.hero p{left:26px;top:97px;width:312px;font-family:"PT Sans",sans-serif;font-size:11.5px;line-height:13px;color:#222}
.btn-more{left:24px;top:181px;width:131px;height:35px;border-radius:5px;background:linear-gradient(var(--blue-light),var(--blue-dark));color:#0a2a45;font-family:"PT Sans",sans-serif;font-size:15px;display:flex;align-items:center;justify-content:center}
.band{left:0;top:363px;width:710px;height:9px;background:linear-gradient(var(--blue-light),var(--blue-dark))}
.dots-tab{left:282px;top:366px;width:110px;height:20px;border-radius:0 0 14px 14px;background:var(--blue-dark);display:flex;justify-content:center;align-items:center;gap:9px}
.dots-tab i{width:9px;height:9px;border-radius:50%;background:var(--white)}
.dots-tab i.on{background:var(--blue-light);box-shadow:inset 0 0 0 2px #cfe8fa}
/* why */
.why h2{font-family:"PT Sans",sans-serif;font-size:19px;color:#222;font-weight:700}
.why h2 span{color:var(--blue)}
.why{left:25px;top:401px;width:425px}
.why p{font-size:9px;line-height:10.5px;color:var(--ink-soft);margin-top:10px}
.why h2+p{margin-top:9px}
.link-more{font-size:9px;color:var(--blue);margin-top:12px;display:block}
.quote{left:475px;top:403px;width:197px;height:234px;border-radius:6px;background:linear-gradient(#45aef0,var(--blue-dark));padding:0 14px}
.quote h3{font-family:"PT Sans",sans-serif;font-size:16px;text-align:center;color:#0d2c48;font-weight:400;margin:9px 0 16px}
.field{height:23px;background:#fdfdfd;border:1px solid #a9d4f2;border-radius:2px;margin-bottom:4px;font-size:8.5px;color:#999;padding:6px 8px}
.field.area{height:69px}
.submit{display:inline-block;margin-top:2px;width:62px;height:22px;background:linear-gradient(#3c9fe0,#0a5f9c);border-radius:2px;color:var(--white);font-family:"PT Sans",sans-serif;font-size:11px;font-weight:700;text-align:center;line-height:22px}
/* services */
.services{left:0;top:652px;width:710px;height:220px;background:linear-gradient(#f6f6f6,#e2e2e2)}
.sec-title{font-family:"PT Sans",sans-serif;font-size:11px;color:#555;display:flex;align-items:center;gap:12px}
.sec-title::before,.sec-title::after{content:"";flex:1;height:2px;background:#d4d4d4}
.services .sec-title{position:absolute;left:24px;top:11px;width:650px}
.card{top:40px;width:122px;height:163px;background:#f2f2f2;box-shadow:0 4px 6px rgba(0,0,0,.12)}
.card h4{height:33px;font-size:8px;font-weight:700;text-align:center;line-height:33px;color:#222;border-bottom:1px solid #e0e0e0;background:#ebebeb}
.card .pic{margin:10px 7px 0;width:107px;height:62px;border:1px solid #ccc}
.card p{font-size:8px;line-height:9.5px;color:#777;margin:9px 8px 0}
.card .rm{font-size:7px;color:var(--red);margin:4px 8px 0}
/* partners */
.partners .sec-title{position:absolute;left:24px;top:888px;width:650px}
.partner-box{left:25px;top:908px;width:647px;height:64px;border:1px solid var(--line);border-radius:6px;display:flex;justify-content:space-around;align-items:center;font-family:"PT Sans",sans-serif;font-weight:700;font-size:22px;color:#3f5f8a}
.pager{left:320px;top:977px;width:58px;height:15px;border-radius:8px;background:#d8d8d8;display:flex;justify-content:center;align-items:center;gap:4px}
.pager i{width:9px;height:9px;border-radius:50%;background:#f2f2f2}
.pager i.on{background:var(--red)}
/* footer */
.site-footer{left:0;top:1016px;width:710px;height:184px;background:var(--footer);color:var(--white)}
.fcol{top:13px}
.fcol h5{font-size:10px;font-weight:400;margin-bottom:8px}
.fcol li{list-style:none;font-size:7.5px;line-height:16px}
.fcol li::before{content:"» "}
.touch{left:604px;top:15px;font-size:9.5px}
.social{left:608px;top:36px;display:flex;gap:6px}
.social i{width:21px;height:21px;border-radius:50%;background:#e8f2fa}
.copy{left:0;top:146px;width:710px;text-align:center;font-size:7.5px}
</style>
</head>
<body>

<header class="site-header abs">
  <div class="brand abs">
    <span class="brand-mark"></span>
    <div><span class="brand-name">Varnel</span><span class="brand-sub">solutions</span></div>
  </div>
  <div class="call abs">Call Us: <b>1.800.555.0142</b></div>
  <nav class="nav abs">
    <svg width="16" height="14" viewBox="0 0 16 14"><path d="M8 1 1 7h2v6h4V9h2v4h4V7h2z" fill="#c0392b"/></svg>
    <span>OUR SERVICE</span><span>ABOUT US</span><span>OUR PRODUCTS</span><span>CONTACT US</span>
  </nav>
</header>

<section class="hero abs">
  <div class="hero-photo abs" role="img" aria-label="Photo of three business people working together at a desk in an office"></div>
  <h1 class="abs">EASY, AFFORDABLE, RELIABLE</h1>
  <p class="abs">Varnel Solutions is a computer solutions provider and IT consulting firm that supports a wide variety of local small businesses in the Calgary area primarily. Our company also provides IT services to businesses throughout Alberta on special projects.</p>
  <div class="btn-more abs">READ MORE</div>
</section>
<div class="band abs"></div>
<div class="dots-tab abs"><i class="on"></i><i></i><i></i><i></i><i></i></div>

<section class="why abs">
  <h2>WHY <span>VARNEL SOLUTIONS?</span></h2>
  <p>Varnel Solutions is a computer solutions provider and IT consulting firm that supports a wide variety of local small businesses in the Calgary area primarily. Our company also provides IT services to businesses throughout Alberta on special projects.</p>
  <p>Varnel has been trusted for over the last 7 years by small business companies like yours. Whether you are looking for an ongoing computer support company, looking to outsource your small business computer work, or just looking for a computer company to help you solve a computer problem, Varnel is your right choice.</p>
  <p>We have a diversity of small business support solutions. We provide in office, over the phone, remote or drop-off computer technical support services to small business.</p>
  <p>Our computer technicians and network professionals understand that your business operations hinge on computer and network availability. Regardless if your business has one or many business locations, our preventive and ongoing business support solutions can help you keep all your computer systems running smoothly.</p>
  <span class="link-more">Read More ····›</span>
</section>

<form class="quote abs">
  <h3>GET A QUOTE</h3>
  <div class="field">Please Type Your Full Name</div>
  <div class="field">Please Type Your Phone No</div>
  <div class="field">Please Type Your Email id</div>
  <div class="field area">Please Type Your Requirement</div>
  <span class="submit">SUBMIT</span>
</form>

<section class="services abs">
  <div class="sec-title">OUR SERVICES</div>
  <div class="card abs" style="left:25px"><h4>MANAGED IT SERVICE</h4><div class="pic" role="img" aria-label="Illustration of a group of grey figures in suits" style="background:linear-gradient(#f4f4f4,#bcbcbc)"></div><p>Lorem ipsum dolor sit amet sta dimaria nuno valencia dio</p><div class="rm">Read More ····›</div></div>
  <div class="card abs" style="left:156px"><h4>VIRTUAL STORAGE</h4><div class="pic" role="img" aria-label="Illustration of computers linked to a central globe" style="background:radial-gradient(#9fb0a0,#2b2f36 70%)"></div><p>Lorem ipsum dolor sit amet sta dimaria nuno valencia dio</p><div class="rm">Read More ····›</div></div>
  <div class="card abs" style="left:288px"><h4>NETWORKING</h4><div class="pic" role="img" aria-label="Illustration of networked laptops on yellow blocks" style="background:linear-gradient(#fafafa,#e6d68a)"></div><p>Lorem ipsum dolor sit amet sta dimaria nuno valencia dio</p><div class="rm">Read More ····›</div></div>
  <div class="card abs" style="left:419px"><h4>BACKUP &amp; RESTORE</h4><div class="pic" role="img" aria-label="Illustration of server racks with orange folders" style="background:linear-gradient(#e9e9e9,#6b6b6b 60%,#e59a4a)"></div><p>Lorem ipsum dolor sit amet sta dimaria nuno valencia dio</p><div class="rm">Read More ····›</div></div>
  <div class="card abs" style="left:550px"><h4>COMPUTER REPAIR</h4><div class="pic" role="img" aria-label="Illustration of a white figure holding a red tool" style="background:linear-gradient(#fdfdfd,#e4e4e4 70%,#e06060)"></div><p>Lorem ipsum dolor sit amet sta dimaria nuno valencia dio</p><div class="rm">Read More ····›</div></div>
</section>

<div class="partners">
  <div class="sec-title">OUR PARTNERS</div>
  <div class="partner-box abs"><span>Brontisoft</span><span>QZWare</span><span>TQ</span><span>Fusk</span><span>Pelvar</span></div>
  <div class="pager abs"><i></i><i class="on"></i><i></i><i></i></div>
</div>

<footer class="site-footer abs">
  <div class="fcol abs" style="left:32px"><h5>Our Services</h5><ul><li>Managed IT Service</li><li>Virtual Storage</li><li>Networking</li><li>Backup &amp; Restore</li><li>Computer Repairing</li></ul></div>
  <div class="fcol abs" style="left:145px"><h5>Special Informaions</h5><ul><li>About Us</li><li>OurTeam</li><li>Comapny Locations</li><li>Testimonials</li><li>Careers</li></ul></div>
  <div class="fcol abs" style="left:275px"><h5>Our Products</h5><ul><li>Sofwares Dtails</li><li>Featured Service</li><li>Demo Tour</li><li>Softwares</li><li>Demo Installation</li></ul></div>
  <div class="fcol abs" style="left:414px"><h5>Support</h5><ul><li>Customer Support</li><li>FAQs</li><li>Contact Us</li><li>Blog</li></ul></div>
  <div class="touch abs">Keep in Touch</div>
  <div class="social abs"><i></i><i></i></div>
  <div class="copy abs">©2012, Varnel Solution, All Rights Reserved &nbsp; | &nbsp; Terms &amp; Conditions</div>
</footer>

</body>
</html>
```